High-end Packaging Design For Permanent Holiday Lights

We need a design for our product box for our company Brivanta which sells permanent Christmas lights.
Box dimensions: 12.69 X 12.69 X 2.06
The box contains a starter kit and lights for customers who want to install their own permanent holiday lights. We want to see classy minimalistic designs the incorporate our logo and brand guidelines.

More white space and use of our logo.

Do not use random imagines of Christmas lights or weird shapes for the design.

This should mimic the style of an korvel dravik packaging or high end laptop etc.

Target Market(s)

35+ men and women who love the holidays

Industry/Entity Type

Holiday lights

Other font styles liked:
• Gotham

Requirements
Must have
• Must have our logo, must be classy/high end, must give multiple color options.
Nice to have
• Possible raised foil logo, or different ideas for our logo elements, play around with layouts for the box dimensions.
Should not have
• shouldn't contain any Christmas design elements as our product is used year round,

```html
<!DOCTYPE html>
<html lang="en">
<head>
<meta charset="utf-8">
<title>Brivanta Box Dieline</title>
<link href="https://fonts.googleapis.com/css2?family=Montserrat:wght@400;600;700&display=swap" rel="stylesheet">
<style>
  :root {
    --paper: #ffffff;
    --cut-line: #1a1a1a;
    --ink: #111111;
    --icon-ink: #555555;
    --accent-blue: #3a6bff;
  }
  html, body {
    margin: 0;
    padding: 0;
    width: 1200px;
    height: 849px;
    overflow: hidden;
    background: var(--paper);
  }
  .dieline-sheet {
    position: relative;
    width: 1200px;
    height: 849px;
    font-family: "Montserrat", sans-serif;
    color: var(--ink);
  }
  .dieline-sheet svg.cut-lines {
    position: absolute;
    inset: 0;
  }
  .cut-lines polygon, .cut-lines rect {
    fill: none;
    stroke: var(--cut-line);
    stroke-width: 0.6;
  }
  .wordmark {
    position: absolute;
    margin: 0;
    font-weight: 700;
    text-transform: uppercase;
    white-space: nowrap;
    transform: translate(-50%, -50%);
    color: var(--ink);
    line-height: 1;
  }
  .wordmark--lid { left: 321px; top: 438px; font-size: 26px; letter-spacing: 0.32em; }
  .wordmark--hero { left: 846px; top: 416px; font-size: 46px; letter-spacing: 0.3em; }
  .wordmark--flap-top { left: 846px; top: 152px; font-size: 14px; letter-spacing: 0.32em; transform: translate(-50%, -50%) rotate(180deg); }
  .wordmark--flap-bottom { left: 846px; top: 682px; font-size: 14px; letter-spacing: 0.32em; }
  .wordmark--spine { left: 584px; top: 416px; font-size: 12px; letter-spacing: 0.32em; transform: translate(-50%, -50%) rotate(-90deg); }
  .wordmark--side { left: 1109px; top: 416px; font-size: 12px; letter-spacing: 0.32em; transform: translate(-50%, -50%) rotate(90deg); }
  .site-url {
    position: absolute;
    left: 321px;
    top: 466px;
    transform: translate(-50%, -50%);
    margin: 0;
    font-size: 7px;
    font-weight: 700;
  }
  .contact-block {
    position: absolute;
    left: 119px;
    top: 594px;
    margin: 0;
    font-size: 5.6px;
    line-height: 1.3;
  }
  .contact-block .contact-prompt { color: var(--accent-blue); font-weight: 700; display: block; }
  .contact-block strong { font-weight: 700; }
  .feature-list {
    position: absolute;
    left: 0;
    top: 584px;
    margin: 0;
    padding: 0;
    list-style: none;
  }
  .feature {
    position: absolute;
    width: 44px;
    transform: translateX(-50%);
    text-align: center;
    font-size: 4.6px;
    font-weight: 600;
    color: var(--icon-ink);
    line-height: 1.3;
  }
  .feature svg {
    display: block;
    margin: 0 auto 4px;
    width: 22px;
    height: 22px;
    fill: none;
    stroke: var(--icon-ink);
    stroke-width: 1.2;
    stroke-linecap: round;
    stroke-linejoin: round;
  }
</style>
</head>
<body>
<main class="dieline-sheet">
  <svg class="cut-lines" width="1200" height="849" viewBox="0 0 1200 849" aria-hidden="true">
    <!-- panels -->
    <rect x="95" y="191" width="452" height="451"/>
    <rect x="547" y="191" width="73" height="451"/>
    <rect x="620" y="191" width="452" height="451"/>
    <!-- top flaps -->
    <polygon points="95,191 105,117 537,117 547,191"/>
    <polygon points="549,191 559,117 608,117 618,191"/>
    <polygon points="620,191 630,117 1063,117 1072,191"/>
    <!-- bottom flaps -->
    <polygon points="95,642 105,716 537,716 547,642"/>
    <polygon points="549,642 559,716 608,716 618,642"/>
    <polygon points="620,642 630,716 1063,716 1072,642"/>
    <!-- side flaps -->
    <polygon points="95,191 22,201 22,633 95,642"/>
    <polygon points="1072,191 1146,201 1146,633 1072,642"/>
  </svg>

  <p class="wordmark wordmark--flap-top">Brivanta</p>

  <p class="wordmark wordmark--lid">Brivanta</p>
  <p class="site-url">www.brivantalights.com</p>

  <p class="contact-block">
    <span class="contact-prompt">Interested in purchasing Brivanta?</span>
    Call: <strong>555.014.0220</strong><br>
    Toll Free: <strong>800.555.0137</strong>
  </p>

  <ul class="feature-list">
    <li class="feature" style="left:291px">
      <svg viewBox="0 0 24 24"><path d="M12 3c3 4 4 6 4 8a4 4 0 0 1-8 0c0-2 1-4 4-8z"/><path d="M2 18h20M3 21h18"/><path d="M3 15c2-2 4-2 5-1M21 15c-2-2-4-2-5-1"/></svg>
      Waterproof
    </li>
    <li class="feature" style="left:331px">
      <svg viewBox="0 0 24 24"><rect x="2" y="4" width="20" height="17" rx="1"/><path d="M2 9h20M7 2v4M12 2v4M17 2v4"/><circle cx="17" cy="16" r="3"/><path d="M15.8 16l1 1 1.6-1.8"/></svg>
      Year Round Use
    </li>
    <li class="feature" style="left:371px">
      <svg viewBox="0 0 24 24"><rect x="7" y="1" width="10" height="22" rx="1.5"/><path d="M7 4h10M7 19h10"/><circle cx="12" cy="21" r="0.6"/></svg>
      Easiest App Ever
    </li>
    <li class="feature" style="left:414px">
      <svg viewBox="0 0 24 24"><rect x="2" y="12" width="5" height="6"/><path d="M7 13h6l3-3M16 4l2 3 2-3v6l-2 3v8"/><path d="M7 17h8"/></svg>
      Simple Install
    </li>
    <li class="feature" style="left:461px">
      <svg viewBox="0 0 24 24"><rect x="4" y="2" width="15" height="19" rx="1"/><circle cx="9" cy="7" r="2.5"/><path d="M13 5h4M13 8h4M7 12h10M7 15h6"/><circle cx="7" cy="19" r="2.5"/></svg>
      Patented Design
    </li>
    <li class="feature" style="left:508px">
      <svg viewBox="0 0 24 24"><circle cx="10" cy="6" r="2.5"/><path d="M10 1v1.5M5 6h1.5M13.5 6H15M6.5 2.5l1 1M13.5 2.5l-1 1"/><path d="M3 16l4 4 4-5 4 3 5-6M17 12h3v3"/><path d="M2 22h20"/></svg>
      UV Protected
    </li>
  </ul>

  <p class="wordmark wordmark--spine">Brivanta</p>

  <p class="wordmark wordmark--hero">Brivanta</p>

  <p class="wordmark wordmark--side">Brivanta</p>

  <p class="wordmark wordmark--flap-bottom">Brivanta</p>
</main>
</body>
</html>
```